Flyer Design for mobile emergency tool and vehicle up-fitting services company

trifold flyer design for a uplifting company that does poly - plastic manufacturing for FIRE, EMS and POLICE vehicles. We design and manufacture poly systems for tools, custom storage solutions. We install vehicle lifts, lights, sirens, consoles, cabinets etc. We use CNC to design custom mounting projects for first responders

Target Market(s)

FIRE, EMS, MILITARY and POLICE

Industry/Entity Type

emergency services

Font styles to use
Serif

Colors
EB3D1F
EC4F4E
F09395
F8D3D4
FCEDEE

Requirements
Must have
• multiple pictures
Nice to have
• background design that is related to my current market

```html
<!DOCTYPE html>
<html lang="en">
<head>
<meta charset="utf-8">
<title>Vanguard Trifold Flyer</title>
<link href="https://fonts.googleapis.com/css2?family=Stardos+Stencil:wght@700&family=Oswald:wght@500&family=Roboto:ital,wght@0,400;1,700&display=swap" rel="stylesheet">
<style>
  :root {
    --backdrop: #e4dbcf;
    --ink: #0a0a0a;
    --alert-red: #e30d16;
    --deep-red: #b3060d;
    --navy: #0d0f8c;
    --white: #ffffff;
    --steel: #5c5f66;
    --sky: #3a78c9;
  }
  * { box-sizing: border-box; margin: 0; padding: 0; }
  html, body { width: 818px; height: 1200px; overflow: hidden; background: var(--backdrop); }
  .canvas { position: relative; width: 818px; height: 1200px; }
  .spread { position: absolute; left: 20px; width: 778px; height: 540px; overflow: hidden;
            box-shadow: 0 10px 24px rgba(0,0,0,.18); }
  .spread--outside { top: 30px; }
  .spread--inside { top: 630px; }
  .block { position: absolute; }
  .photo { position: absolute; }
  .panel-dark { background: var(--ink); }
  .panel-red { background: var(--alert-red); }

  .mission-text { font-family: "Roboto", sans-serif; font-style: italic; font-weight: 700;
    color: var(--white); font-size: 15px; line-height: 1.3; text-transform: uppercase;
    padding: 46px 34px 0 34px; }

  .services { display: flex; flex-direction: column; align-items: center; justify-content: center;
    text-align: center; color: var(--white); font-family: "Stardos Stencil", serif; font-weight: 700; }
  .services__list { font-size: 21px; line-height: 1.1; text-transform: uppercase; }
  .services__rule { width: 150px; height: 2px; background: rgba(255,255,255,.7); margin: 14px 0; }
  .services__contact { font-size: 18px; line-height: 1.25; }

  .cover { background: linear-gradient(160deg, #1a0506 0%, #0b0b0d 45%, #050505 100%); }
  .brand { position: absolute; top: 40px; right: 22px; display: flex; align-items: center; gap: 10px; }
  .brand__dot { width: 34px; height: 34px; border-radius: 50%; background: var(--white); }
  .brand__name { font-family: "Stardos Stencil", serif; font-weight: 700; color: var(--white);
    font-size: 22px; letter-spacing: 1px; }
  .cover__stop { position: absolute; top: 120px; width: 100%; text-align: center;
    font-family: "Stardos Stencil", serif; font-weight: 700; font-size: 76px; color: var(--alert-red); line-height: 1; }
  .cover__lead { position: absolute; top: 205px; width: 100%; text-align: center;
    font-family: "Oswald", sans-serif; font-weight: 500; font-size: 22px; line-height: 1.1;
    color: var(--white); text-transform: uppercase; }
  .cover__rule { position: absolute; top: 290px; left: 40px; right: 40px; height: 2px;
    background: linear-gradient(90deg, transparent, var(--alert-red), transparent); }
  .cover__promise { position: absolute; top: 305px; width: 100%; text-align: center;
    font-family: "Stardos Stencil", serif; font-weight: 700; font-size: 28px; line-height: 1.05;
    color: var(--white); text-transform: uppercase; }
  .cover__band { position: absolute; left: 0; right: 0; bottom: 0; height: 100px; background: var(--navy);
    display: flex; align-items: center; justify-content: center; text-align: center; padding: 0 26px;
    font-family: "Oswald", sans-serif; font-weight: 500; font-size: 14px; line-height: 1.25;
    color: #cfd2ff; text-transform: uppercase; }

  .body-text { font-family: "Roboto", sans-serif; font-weight: 400; color: var(--white);
    font-size: 13px; line-height: 1.35; }
  .body-text--left { padding: 60px 30px 0 30px; }
  .body-text--right { padding: 44px 28px 0 28px; }
</style>
</head>
<body>
<div class="canvas">

  <section class="spread spread--outside">
    <div class="block panel-dark" style="left:0;top:0;width:259px;height:270px;">
      <p class="mission-text">Vanguard is owned and operated by first responders and our company is dedicated to the brothers and sisters that are on the frontline every day.</p>
    </div>
    <div class="photo" role="img" aria-label="Collage of organized tool compartments on fire apparatus"
         style="left:0;top:270px;width:259px;height:270px;background:linear-gradient(135deg,#8a1a1e,#4a4c52 45%,#c9a21a 75%,#3a3a3e);"></div>

    <div class="photo" role="img" aria-label="Rescue tools mounted in a vehicle compartment"
         style="left:259px;top:0;width:260px;height:300px;background:linear-gradient(160deg,#2a2a2e,#7d8088 50%,#b4b6bb);"></div>
    <div class="block panel-red services" style="left:259px;top:300px;width:260px;height:240px;">
      <p class="services__list">We install<br>vehicle lifts,<br>lights, sirens,<br>consoles,<br>cabinets</p>
      <div class="services__rule"></div>
      <p class="services__contact">0123 456 7890<br>www.website.com</p>
    </div>

    <div class="block cover" style="left:519px;top:0;width:259px;height:540px;" role="img" aria-label="Emergency vehicle at night with lit signage">
      <div class="brand"><span class="brand__dot"></span><span class="brand__name">VANGUARD</span></div>
      <p class="cover__stop">STOP</p>
      <p class="cover__lead">Putting your<br>emergency vehicles<br>out of service</p>
      <div class="cover__rule"></div>
      <p class="cover__promise">We will<br>come to you!</p>
      <div class="cover__band">We have a mobile fabrication unit that will come onsite for custom installs</div>
    </div>
  </section>

  <section class="spread spread--inside">
    <div class="block panel-dark" style="left:0;top:0;width:259px;height:240px;">
      <p class="body-text body-text--left">Vanguard Apparatus understands the importance of keeping your first out tools safe, secure, and easily accessible. The task of organizing and securing all of your equipment while utilizing all of your compartment space can be complicated. Vanguard makes it easy with a line of products custom built for your needs.</p>
    </div>
    <div class="photo" role="img" aria-label="Red response truck with open rear storage compartments"
         style="left:0;top:240px;width:259px;height:300px;background:linear-gradient(150deg,#7aa6d8,#c21820 45%,#2a2a2c);"></div>

    <div class="photo" role="img" aria-label="Open truck compartment with custom tool mounts under blue sky"
         style="left:259px;top:0;width:260px;height:540px;background:linear-gradient(180deg,#3a78c9 0%,#1b1b1e 35%,#2b2d32 60%,#4a6b3a 85%,#8a8a86);"></div>

    <div class="block panel-red" style="left:519px;top:0;width:259px;height:260px;">
      <p class="body-text body-text--right">It is our duty to produce innovative tool-specific mounting solutions and organizing products to utilize every square inch of the compartment space. All of Vanguard's components are manufactured from rugged, durable, chemical-resistant HDPE (high density polyethylene) material. This material is non-toxic, has a high degree of stability, and resists degradation.</p>
    </div>
    <div class="photo" role="img" aria-label="Pickup bed with slide-out storage drawers"
         style="left:519px;top:260px;width:259px;height:280px;background:linear-gradient(170deg,#4f8fd6,#9ab3c8 35%,#3a3b40 60%,#8d8a80);"></div>
  </section>

</div>
</body>
</html>
```